KELU Nature Soap

We need to design new product Nature and medicative Soap.Made in Malaysia
* 100% natural.
* made from nature Tropic oil.
* Very effective for Acne & Skin irritation
* size 100 Gm.
* Use for all skin types including sensitive skin
* Name of the product " KELU Soap"

Reason: please I need to extended since I haven't receive any suitable design for my project

Target Market(s)

International

Industry/Entity Type

Hair And Beauty

Font styles to use
Serif

Colors
33a6d7
abd037
fbed22

Requirements
Must have
• * must have English- Arabic ingredient
• * Very effective for Acne & Skin irritation
Nice to have
• * some things related to natural (water,tree,face..)
• * Show faces picture (after - before)

```html
<!DOCTYPE html>
<html lang="en">
<head>
<meta charset="utf-8">
<title>KELU Soap – Label</title>
<link rel="stylesheet" href="https://fonts.googleapis.com/css2?family=Marcellus&family=Oranienbaum&display=swap">
<style>
  :root {
    --sky-top: #6fcdf0;
    --sky-mid: #bfeafb;
    --sky-haze: #eaf8fd;
    --sea: #33a6d7;
    --sea-deep: #2a7fd0;
    --title-blue: #123a9c;
    --mark-blue: #1a4fb0;
    --glow-yellow: #fbed22;
    --claim-green: #1a9a2e;
    --band-light: #6fc6ec;
    --band-dark: #2f8fd0;
    --soap-top: #f2c9a6;
    --soap-bottom: #f6b38a;
    --leaf-green: #3a9e3c;
    --coco-brown: #a4532a;
    --white: #ffffff;
  }
  * { margin: 0; padding: 0; box-sizing: border-box; }
  html, body { width: 1200px; height: 840px; overflow: hidden; background: #fff; }
  .label {
    position: relative;
    width: 1200px;
    height: 840px;
    overflow: hidden;
    background: linear-gradient(180deg, var(--sky-top) 0%, var(--sky-mid) 30%, var(--sky-haze) 50%, var(--sky-mid) 66%, var(--sea) 100%);
  }
  .sea-waves {
    position: absolute; left: 0; top: 472px; width: 1200px; height: 292px;
    background: linear-gradient(180deg, rgba(51,166,215,0) 0%, rgba(51,166,215,0.55) 40%, var(--sea-deep) 100%);
  }
  .palm-leaf {
    position: absolute; left: 808px; top: 0; width: 392px; height: 248px;
    background: radial-gradient(ellipse at 75% 20%, var(--leaf-green) 0%, rgba(58,158,60,0.6) 45%, rgba(58,158,60,0) 75%);
  }
  .soap-bar {
    position: absolute; left: 646px; top: 218px; width: 458px; height: 382px;
    border-radius: 12px;
    background: linear-gradient(180deg, var(--soap-top), var(--soap-bottom));
  }
  .coconuts {
    position: absolute; left: 768px; top: 492px; width: 384px; height: 268px;
    border-radius: 24px;
    background: radial-gradient(ellipse at 50% 55%, #c7733f 0%, var(--coco-brown) 55%, rgba(164,83,42,0) 80%);
  }
  .brand-mark {
    position: absolute; left: 240px; top: 30px; width: 150px;
    display: flex; flex-direction: column; align-items: center; gap: 14px;
  }
  .brand-dot { width: 78px; height: 78px; border-radius: 50%; background: var(--mark-blue); }
  .brand-name {
    font-family: "Marcellus", serif; font-size: 28px; letter-spacing: 4px;
    color: var(--mark-blue);
  }
  .product-title {
    position: absolute; left: 98px; top: 196px; width: 480px;
    font-family: "Marcellus", serif; font-weight: 400; font-size: 98px; line-height: 1;
    color: var(--title-blue); letter-spacing: -3px; white-space: nowrap;
    text-shadow: 0 0 3px var(--glow-yellow), 0 0 2px var(--glow-yellow);
  }
  .claims {
    position: absolute; left: 18px; width: 620px; text-align: center;
    font-family: "Oranienbaum", serif; font-size: 38px; line-height: 38px;
    color: var(--claim-green); white-space: nowrap;
    text-shadow: 0 0 6px var(--white), 0 0 10px var(--white);
  }
  .claim-acne { top: 430px; }
  .claim-skin { top: 548px; }
  .claim-rule {
    position: absolute; left: 54px; top: 522px; width: 554px; height: 3px;
    background: var(--claim-green);
  }
  .footer-band {
    position: absolute; left: 0; top: 764px; width: 1200px; height: 44px;
    background: var(--band-light);
  }
  .footer-base {
    position: absolute; left: 0; top: 808px; width: 1200px; height: 32px;
    background: var(--band-dark);
  }
  .footer-text {
    position: absolute; top: 764px; height: 44px; line-height: 46px;
    font-family: "Oranienbaum", serif; font-size: 38px; color: var(--white); white-space: nowrap;
  }
  .footer-natural { left: 108px; }
  .footer-divider { left: 410px; font-size: 26px; }
  .footer-oil { left: 586px; }
</style>
</head>
<body>
<main class="label">
  <div class="sea-waves" role="img" aria-label="Flowing blue sea waves across the lower part of the label"></div>
  <div class="palm-leaf" role="img" aria-label="Green palm leaf hanging in from the top right corner"></div>
  <div class="soap-bar" role="img" aria-label="Peach coloured bar of natural soap with light speckles"></div>
  <div class="coconuts" role="img" aria-label="Whole coconut and halved coconut with green leaves"></div>

  <div class="brand-mark">
    <span class="brand-dot"></span>
    <span class="brand-name">KELU</span>
  </div>

  <h1 class="product-title">KELU SOAP</h1>

  <p class="claims claim-acne">VERY EFFECTIVE FOR ACNE &amp;<br>SKIN IRRITATION</p>
  <div class="claim-rule"></div>
  <p class="claims claim-skin">USE FOR ALL SKIN TYPES INCLUDING<br>SENSITIVE SKIN</p>

  <div class="footer-band"></div>
  <div class="footer-base"></div>
  <span class="footer-text footer-natural">100% NATURA</span>
  <span class="footer-text footer-divider">-------</span>
  <span class="footer-text footer-oil">MADE FROM NATURE TROPIC OIL</span>
</main>
</body>
</html>
```